New Business Card Design Project

We are a spa looking to create a professional elegant business card for a spa mainly black and white with a splash of lime green. This card will be two sided - the front side will have an image, the logo, and the spa's information - the back side will have a promotion for new customers - NEW CUSTOMERS $20 OFF

Look and feel: chic, modern, and spa-ish.
Information to be included:
Therapist Name
Therapist specialty
Address: 5174 Marlowe Ave, Beverly Hills CA 90211
Phone: (310) 482-3957

Let me know if you have any questions!

Thank you

Industry/Entity Type

Business

```html
<!DOCTYPE html>
<html lang="en">
<head>
<meta charset="utf-8">
<title>Willow Day Spa – Business Card</title>
<link href="https://fonts.googleapis.com/css2?family=Arimo:wght@400;700&family=Montserrat:wght@600&display=swap" rel="stylesheet">
<style>
  :root {
    --lime: #8dc63f;
    --lime-bright: #9bd53a;
    --black: #0d0d0d;
    --ink: #1a1a1a;
    --white: #ffffff;
    --backdrop: #e8e8e5;
    --photo-light: #f1ece4;
    --photo-mid: #d9c2ae;
    --photo-green: #7fbf3a;
  }
  * { box-sizing: border-box; margin: 0; padding: 0; }
  html, body { width: 1200px; height: 784px; overflow: hidden; }
  body {
    background: var(--backdrop);
    font-family: "Arimo", Arial, sans-serif;
    position: relative;
  }
  .card {
    position: absolute;
    left: 290px;
    width: 620px;
    height: 354px;
    border-radius: 4px;
    overflow: hidden;
    box-shadow: 0 6px 18px rgba(0,0,0,0.18);
  }

  /* Back side */
  .card-back {
    top: 24px;
    background: radial-gradient(ellipse at 50% 40%, #1e1e1e 0%, var(--black) 70%);
  }
  .card-back .seal {
    position: absolute;
    left: 200px; top: 28px;
    width: 220px; height: 220px;
    border-radius: 50%;
    border: 3px solid rgba(255,255,255,0.05);
  }
  .card-back .offer {
    position: absolute;
    left: 0; right: 0; top: 126px;
    text-align: center;
    font-family: "Montserrat", Arial, sans-serif;
    font-weight: 600;
    font-size: 22px;
    letter-spacing: 7px;
    color: var(--lime-bright);
  }

  /* Front side */
  .card-front {
    top: 406px;
    background: var(--white);
  }
  .card-front .photo {
    position: absolute;
    left: 300px; top: 0;
    width: 320px; height: 290px;
    background:
      linear-gradient(160deg, var(--photo-green) 0%, rgba(127,191,58,0) 35%),
      linear-gradient(180deg, var(--photo-light) 0%, var(--photo-mid) 100%);
  }
  .card-front .base-band {
    position: absolute;
    left: 0; right: 0; top: 290px;
    height: 38px;
    background: var(--black);
  }
  .card-front .base-line {
    position: absolute;
    left: 0; right: 0; top: 332px;
    height: 5px;
    background: var(--lime);
  }
  .brand {
    position: absolute;
    left: 40px; top: 26px;
    width: 150px; height: 150px;
    border-radius: 50%;
    border: 3px solid var(--ink);
    display: flex;
    align-items: center;
    justify-content: center;
    text-align: center;
  }
  .brand-name {
    font-size: 20px;
    font-weight: 700;
    line-height: 1.2;
    color: var(--ink);
    letter-spacing: 1px;
  }
  .therapist-name {
    position: absolute;
    left: 40px; top: 188px;
    font-size: 19px;
    font-weight: 700;
    color: var(--lime);
  }
  .therapist-specialty {
    position: absolute;
    left: 40px; top: 212px;
    font-size: 13px;
    color: var(--ink);
  }
  .contact {
    position: absolute;
    left: 40px; top: 232px;
    font-size: 17px;
    line-height: 20px;
    color: var(--ink);
    list-style: none;
  }
  .contact li {
    display: flex;
    align-items: flex-start;
    gap: 6px;
  }
  .contact .icon {
    width: 16px; height: 16px;
    margin-top: 2px;
    flex: none;
  }
  .contact .icon path { fill: var(--lime); }
  .contact .icon-spacer { width: 16px; flex: none; }
</style>
</head>
<body>

  <section class="card card-back">
    <div class="seal"></div>
    <p class="offer">NEW CUSTOMERS $20 OFF</p>
  </section>

  <section class="card card-front">
    <div class="photo" role="img" aria-label="Relaxed woman resting on a rolled towel with a pink lily, bamboo and hot stones"></div>
    <div class="base-band"></div>
    <div class="base-line"></div>

    <div class="brand">
      <span class="brand-name">Willow<br>Day Spa</span>
    </div>

    <p class="therapist-name">Therapist Name</p>
    <p class="therapist-specialty">Therapist specialty</p>

    <ul class="contact">
      <li>
        <svg class="icon" viewBox="0 0 24 24" aria-hidden="true"><path d="M6.6 10.8a15.1 15.1 0 0 0 6.6 6.6l2.2-2.2a1 1 0 0 1 1-.25 11.4 11.4 0 0 0 3.6.57 1 1 0 0 1 1 1V20a1 1 0 0 1-1 1A17 17 0 0 1 3 4a1 1 0 0 1 1-1h3.5a1 1 0 0 1 1 1c0 1.25.2 2.45.57 3.57a1 1 0 0 1-.25 1z"/></svg>
        <span>(310) 482-3957</span>
      </li>
      <li>
        <svg class="icon" viewBox="0 0 24 24" aria-hidden="true"><path d="M12 3 2 12h3v8h5v-6h4v6h5v-8h3z"/></svg>
        <span>5174 Marlowe Ave,</span>
      </li>
      <li>
        <span class="icon-spacer"></span>
        <span>Beverly Hills CA 90211</span>
      </li>
    </ul>
  </section>

</body>
</html>
```